Online Prescription Eyewear Company Needs a Website

We sell prescription glasses starting at $99 with Free Shipping. We have over 300 different styles and colors.

Our website is under construction and we need an amazing landing page to kick things off. Our brand is called VARNO and our website is called VARNOEYEWEAR.EXAMPLE.

We are a website similar to
kestonhale.example
shoprudyplume.example
Brova.example

We sell prescription glasses starting at $99 with Free Shipping. Options to upgrade to Anti Glare, Blue light Protection, Shadeshift or High Index.

We also have a lens replacement option and will change out old prescription lenses starting at $79 with Free Shipping.

Important!!

We Love the layout of https://tessbrundle.example/ . We are hoping to use Tess Brundle as a templet. The closest page that looks like Tess Brundle will win.

We do not prefer the pink. Substitute the pink with Navy Teal.

We also prefer a better footer than Tess Brundle

The landing page should include, Gender neutral and Colors are Black, White, Gray, Navy Teal

We prefer a Simple, Clean Look.

The Header should be similar to kestonhale.example

The Landing page look very similar to Tess Brundle with large banner with quad banner below to follow.

We need better footer. Here are the menu items for footer.

PRODUCTS
All Frames
Mens Frames
Womens Frames
Best Sellers
New Arrivals

ORDER
Single Vision Lenses
Blue Light Blocking Computer Lenses
High Index Lenses
Shadeshift Lenses
Reading Lenses

INFORMATION
Track Order
About Us
Contact Us
Returns
Warranty
FAQ

Target Market(s)

20-40 yo Male/Female wears glasses

Industry/Entity Type

Eyewear

Number of Pages Required

1 page

Font styles to use
Sans Serif

Colors
333333
5c5c5c
919191
b2b2b2
dfdfdf
f5f5f5
1b1b1b
474747
3276b5

Requirements
Must have
• The Landing page look very similar to Tess Brundle.
• Substitute the pink secondary color for Navy Teal
• Should have main Banner with Person wearing glasses. Then the quad banner below should highlight the box with glasses, glasses, etc.
Nice to have
• i have a pixel vault account, so if you find some awesome pictures I can purchase them if they fit in the site.

```html
<!DOCTYPE html>
<html lang="en">
<head>
<meta charset="utf-8">
<title>VARNO — Prescription Eyewear</title>
<link rel="stylesheet" href="https://fonts.googleapis.com/css2?family=Titillium+Web:wght@300;400;600;700&display=swap">
<style>
  :root {
    --ink: #333333;
    --ink-dark: #1b1b1b;
    --ink-mid: #474747;
    --grey-5c: #5c5c5c;
    --grey-91: #919191;
    --grey-b2: #b2b2b2;
    --line: #dfdfdf;
    --paper: #f5f5f5;
    --white: #ffffff;
    --teal: #3276b5;
    --teal-light: #5f9bd3;
    --star-light: #8fb4d8;
    --font: "Titillium Web", "Helvetica Neue", Arial, sans-serif;
  }
  * { box-sizing: border-box; margin: 0; padding: 0; }
  html, body { width: 1200px; height: 2270px; overflow: hidden; background: var(--white); }
  body { position: relative; font-family: var(--font); color: var(--ink); }

  /* Header */
  .site-header { position: absolute; left: 0; top: 0; width: 1200px; height: 59px; background: var(--paper); box-shadow: 0 2px 4px rgba(0,0,0,.12); z-index: 3; }
  .brand-box { position: absolute; left: 39px; top: 0; width: 108px; height: 59px; background: var(--ink-dark); color: var(--white); font-size: 24px; font-weight: 400; letter-spacing: 2px; display: flex; align-items: center; justify-content: center; }
  .main-nav a { position: absolute; top: 8px; font-size: 24px; color: var(--ink); text-decoration: none; letter-spacing: 1.8px; }
  .search { position: absolute; left: 870px; top: 18px; width: 135px; height: 23px; border: 1px solid var(--line); background: var(--white); font-size: 11px; color: var(--grey-91); padding: 3px 8px; }
  .search svg { position: absolute; right: 8px; top: 5px; }
  .divider-v { position: absolute; top: 18px; width: 1px; height: 22px; background: var(--grey-b2); }
  .cart { position: absolute; left: 1032px; top: 19px; }
  .sign-in { position: absolute; left: 1086px; top: 16px; font-size: 18px; font-weight: 700; color: var(--teal); letter-spacing: 1.5px; }

  /* Hero */
  .hero { position: absolute; left: 0; top: 59px; width: 1200px; height: 430px; background: linear-gradient(90deg, #c9c4bd 0%, #e3e0db 40%, #d8d2cc 65%, #b3a79e 100%); }
  .hero-title { position: absolute; left: 64px; top: 56px; font-size: 56px; font-weight: 600; letter-spacing: 4.5px; color: var(--ink); line-height: 1; }
  .hero-sub { position: absolute; left: 66px; top: 124px; font-size: 38px; font-weight: 400; letter-spacing: 2.5px; color: var(--ink); line-height: 1; }
  .hero-sub small { font-size: 24px; }
  .btn { position: absolute; background: var(--teal); color: var(--white); font-family: var(--font); display: flex; align-items: center; justify-content: center; box-shadow: 2px 3px 4px rgba(0,0,0,.3); letter-spacing: 1px; white-space: nowrap; }
  .hero .btn { left: 68px; top: 212px; width: 267px; height: 55px; font-size: 28px; }
  .hero-arrow { position: absolute; top: 199px; }

  /* Quad */
  .tile { position: absolute; width: 540px; height: 325px; overflow: hidden; box-shadow: 0 0 8px rgba(0,0,0,.08); }
  .tile-photo { position: absolute; inset: 0; }
  .tile-title { position: absolute; left: 38px; top: 176px; font-size: 54px; font-weight: 600; letter-spacing: 6px; line-height: 1; }
  .tile-band { position: absolute; left: 0; bottom: 0; width: 100%; height: 73px; background: rgba(255,255,255,.72); }
  .tile-note { position: absolute; left: 36px; top: 28px; font-size: 13px; font-weight: 600; letter-spacing: 1.5px; color: var(--ink-dark); }
  .tile .btn { left: 365px; top: 23px; width: 133px; height: 28px; font-size: 15px; box-shadow: 1px 2px 3px rgba(0,0,0,.25); letter-spacing: .5px; }
  .on-light { color: var(--ink); }
  .on-dark { color: var(--white); }

  /* Popular */
  .section-title { position: absolute; left: 0; width: 1200px; text-align: center; font-size: 56px; font-weight: 400; letter-spacing: 6px; color: var(--ink); }
  .product { position: absolute; top: 1330px; width: 345px; height: 280px; }
  .swatches { position: absolute; top: 8px; display: flex; gap: 13px; }
  .swatch { width: 33px; height: 19px; position: relative; }
  .swatch.active::after { content: ""; position: absolute; left: 0; bottom: -7px; width: 33px; height: 2px; background: var(--teal); }
  .frame-photo { position: absolute; left: 0; top: 62px; width: 100%; height: 115px; border-radius: 50px; }
  .product-name { position: absolute; top: 190px; font-size: 28px; font-weight: 600; letter-spacing: 2px; color: var(--ink-dark); }
  .product-price { position: absolute; top: 190px; font-size: 28px; font-weight: 600; letter-spacing: 2px; color: var(--teal); }
  .stars { position: absolute; top: 236px; font-size: 28px; letter-spacing: -1px; color: var(--teal); line-height: 1; }
  .stars .off { color: var(--star-light); }
  .more-btn { left: 466px; top: 1636px; width: 268px; height: 56px; font-size: 28px; background: linear-gradient(90deg, var(--teal), var(--teal-light)); }

  /* Newsletter */
  .newsletter { position: absolute; left: 0; top: 1772px; width: 1200px; height: 176px; background: var(--paper); }
  .newsletter h2 { position: absolute; top: 20px; width: 100%; text-align: center; font-size: 32px; font-weight: 400; letter-spacing: 2.6px; color: var(--ink-mid); line-height: 1.3; }
  .newsletter p { position: absolute; top: 58px; width: 100%; text-align: center; font-size: 25px; letter-spacing: 1.5px; color: var(--ink); line-height: 1.3; }
  .mail-input { position: absolute; left: 422px; top: 97px; width: 341px; height: 41px; background: var(--white); border: 1px solid var(--line); font-size: 19px; color: var(--grey-b2); padding: 6px 36px; letter-spacing: 1px; }
  .newsletter .btn { left: 767px; top: 97px; width: 176px; height: 41px; font-size: 25px; box-shadow: none; }

  /* Footer */
  .footer-col { position: absolute; top: 1982px; }
  .footer-col h3 { font-size: 24px; font-weight: 700; letter-spacing: 2.2px; color: var(--ink); margin-bottom: 6px; line-height: 1.3; }
  .footer-col li { list-style: none; font-size: 18px; line-height: 22.6px; letter-spacing: 2px; color: var(--ink-dark); }
  .footer-split { position: absolute; left: 861px; top: 1993px; width: 2px; height: 184px; background: var(--line); }
  .mini-label { font-size: 10px; font-weight: 700; color: var(--ink-mid); letter-spacing: .5px; }
  .socials { display: flex; gap: 15px; margin-top: 6px; }
  .socials span { width: 26px; height: 26px; border-radius: 50%; background: var(--ink); display: block; }
  .phone { font-size: 12px; font-weight: 700; letter-spacing: 1px; color: var(--ink-dark); }
  .footer-brand { position: absolute; left: 937px; top: 2144px; width: 127px; height: 67px; background: var(--ink-mid); color: var(--white); font-size: 28px; font-weight: 400; letter-spacing: 2px; display: flex; align-items: center; justify-content: center; }
  .footer-rule { position: absolute; left: 38px; top: 2222px; width: 1124px; height: 1px; background: var(--line); }
  .copyright { position: absolute; top: 2244px; width: 1200px; text-align: center; font-size: 12px; letter-spacing: 1px; color: var(--ink-dark); }
</style>
</head>
<body>

<header class="site-header">
  <div class="brand-box">VARNO</div>
  <nav class="main-nav">
    <a style="left:186px">Home</a>
    <a style="left:303px">Glasses</a>
    <a style="left:443px">Lens</a>
    <a style="left:546px">Informations</a>
  </nav>
  <div class="search">Search
    <svg width="12" height="12" viewBox="0 0 12 12"><circle cx="5" cy="5" r="3.6" fill="none" stroke="#333" stroke-width="1.6"/><line x1="7.6" y1="7.6" x2="11" y2="11" stroke="#333" stroke-width="1.8"/></svg>
  </div>
  <div class="divider-v" style="left:1025px"></div>
  <svg class="cart" width="26" height="22" viewBox="0 0 26 22"><path d="M1 2h4l3 12h13l3-9H7" fill="none" stroke="#333" stroke-width="2.2"/><path d="M7 5h17l-3 9H9z" fill="#333"/><circle cx="10" cy="19" r="2" fill="#333"/><circle cx="19" cy="19" r="2" fill="#333"/></svg>
  <div class="divider-v" style="left:1070px"></div>
  <div class="sign-in">SIGN IN</div>
</header>

<section class="hero" role="img" aria-label="Smiling young man wearing black frame glasses, talking on a phone in front of a stone building">
  <h1 class="hero-title">Prescription Glasses</h1>
  <div class="hero-sub"><small>at</small> $99 <small>and</small> Free Shipping</div>
  <div class="btn">Go Shopping</div>
  <svg class="hero-arrow" style="left:18px" width="16" height="26" viewBox="0 0 16 26"><path d="M13 2L3 13l10 11" fill="none" stroke="#7a7a7a" stroke-width="4"/></svg>
  <svg class="hero-arrow" style="left:1163px" width="16" height="26" viewBox="0 0 16 26"><path d="M3 2l10 11L3 24" fill="none" stroke="#7a7a7a" stroke-width="4"/></svg>
</section>

<section class="quad">
  <article class="tile" style="left:38px;top:536px">
    <div class="tile-photo" role="img" aria-label="Smiling couple wearing glasses in a bright loft" style="background:linear-gradient(120deg,#e9ecef 0%,#d6d2cc 50%,#c2b6a8 100%)"></div>
    <h2 class="tile-title on-light">Our Glasses</h2>
    <div class="tile-band"><span class="tile-note">Beautiful glasses at $99 and shipping free</span><div class="btn">Check Glasses</div></div>
  </article>
  <article class="tile" style="left:622px;top:536px">
    <div class="tile-photo" role="img" aria-label="Woman with curly hair wearing glasses and a rust striped blouse" style="background:linear-gradient(90deg,#8a8278 0%,#8f877d 50%,#9a6a4c 72%,#8a8278 100%)"></div>
    <h2 class="tile-title on-dark">Our Lens</h2>
    <div class="tile-band"><span class="tile-note">Check our lens and find yours</span><div class="btn">Check Lens</div></div>
  </article>
  <article class="tile" style="left:38px;top:876px">
    <div class="tile-photo" role="img" aria-label="Smiling man in glasses and a denim shirt before a brick wall" style="background:linear-gradient(90deg,#4a3426 0%,#6b4a34 35%,#7e96b3 60%,#7a4a38 100%)"></div>
    <h2 class="tile-title on-dark">Styles</h2>
    <div class="tile-band"><span class="tile-note">Browse our 300+ styles and options</span><div class="btn">Browse styles</div></div>
  </article>
  <article class="tile" style="left:622px;top:876px">
    <div class="tile-photo" role="img" aria-label="Woman with long auburn hair wearing tortoiseshell glasses" style="background:linear-gradient(90deg,#ffffff 0%,#ffffff 45%,#d9b59a 70%,#f4f2f0 100%)"></div>
    <h2 class="tile-title on-light">Upgrades</h2>
    <div class="tile-band"><span class="tile-note">We provide several upgrade options</span><div class="btn">Check Upgrades</div></div>
  </article>
</section>

<section class="popular">
  <h2 class="section-title" style="top:1250px">Popular Hits</h2>

  <div class="product" style="left:38px">
    <div class="swatches" style="left:184px"><span class="swatch active" style="background:#f0d792"></span><span class="swatch" style="background:#1b1416"></span><span class="swatch" style="background:#3276b5"></span></div>
    <div class="frame-photo" role="img" aria-label="Round striped tortoiseshell frames" style="background:radial-gradient(ellipse at center,#d9d1b0 0%,#f3f0e6 60%,#ffffff 100%)"></div>
    <div class="product-name" style="left:30px">Marlow C3</div>
    <div class="product-price" style="left:258px">$75</div>
    <div class="stars" style="left:30px">★★★★<span class="off">★</span></div>
  </div>

  <div class="product" style="left:433px">
    <div class="swatches" style="left:184px"><span class="swatch" style="background:#f0d792"></span><span class="swatch active" style="background:#1b1416"></span><span class="swatch" style="background:#3276b5"></span></div>
    <div class="frame-photo" role="img" aria-label="Cat-eye frames fading from dark red to blue" style="background:radial-gradient(ellipse at center,#c8cfdc 0%,#ece9ef 60%,#ffffff 100%)"></div>
    <div class="product-name" style="left:30px">Marlow C2</div>
    <div class="product-price" style="left:240px">$105</div>
    <div class="stars" style="left:30px">★★★<span class="off">★★</span></div>
  </div>

  <div class="product" style="left:817px">
    <div class="swatches" style="left:186px"><span class="swatch" style="background:#f0d792"></span><span class="swatch" style="background:#1b1416"></span><span class="swatch active" style="background:#fff;border:1px solid #5c5c5c"></span></div>
    <div class="frame-photo" role="img" aria-label="Square clear crystal frames" style="background:radial-gradient(ellipse at center,#eceeee 0%,#f7f7f7 60%,#ffffff 100%)"></div>
    <div class="product-name" style="left:32px">Fenton C1</div>
    <div class="product-price" style="left:260px">$99</div>
    <div class="stars" style="left:32px">★★★★★</div>
  </div>

  <div class="btn more-btn">More Glasses</div>
</section>

<section class="newsletter">
  <h2>Make sure to be informed about our latests offers</h2>
  <p>Subscribe to our Newsletter</p>
  <div class="mail-input">Your mail adress</div>
  <div class="btn">Subscribe</div>
</section>

<footer>
  <div class="footer-col" style="left:129px">
    <h3>PRODUCTS</h3>
    <ul><li>All Frames</li><li>Mens Frames</li><li>Womens Frames</li><li>Best Sellers</li><li>New Arrivals</li></ul>
  </div>
  <div class="footer-col" style="left:360px;width:190px">
    <h3>ORDER</h3>
    <ul><li>Single Vision Lenses</li><li>Blue Light Blocking Computer Lenses</li><li>High Index Lenses</li><li>Shadeshift Lenses</li></ul>
  </div>
  <div class="footer-col" style="left:614px">
    <h3>INFORMATION</h3>
    <ul><li>Track Order</li><li>About Us</li><li>Contact Us</li><li>Returns</li><li>Warranty</li></ul>
  </div>
  <div class="footer-split"></div>
  <div class="footer-col" style="left:935px">
    <h3>GET IN TOUCH</h3>
    <div class="mini-label" style="margin-top:8px">Follow Us on Social Medias</div>
    <div class="socials"><span></span><span></span><span></span><span></span></div>
    <div class="mini-label" style="margin-top:30px">Call Us</div>
    <div class="phone">+8 555-010-24-17</div>
  </div>
  <div class="footer-brand">VARNO</div>
  <div class="footer-rule"></div>
  <div class="copyright">VARNO, Copyright ©2019, All rights Reserved</div>
</footer>

</body>
</html>
```